Accounting business needs a great flyer

I need a flyer for my new business "Ledgerline". I am an individual accountant working for himself on the Sunshine Coast in Queensland Australia. I would like to see designs that communicate reliability and trust. I believe my point of difference is that I am always available to my clients and I will cap my number of clients to ensure I can service them properly.
The main point I want to convey is that most of the time junior employees with little to no experience or unqualified employees do the tax work for the clients and a senior accountant quickly checks the work at the end but never gets to really know the clients business. Accountants in general seem to have a bad reputation for not responding to clients in a timely fashion, whether by email or phone. This is where I intend to differentiate myself. . I have also included some logo's that should go on the flyer.

Target Market(s)

Every small business

Industry/Entity Type

Public Accounting

Requirements
Must have
• Web address: www.ledgerline.com.au
Phone number: 0417 582 396
Attached logos
Reference to: "Do you know who is actually doing your tax?"
Other accounting firms - use junior unqualified staff
- outsource to cheap labour countries
- use tax consultants who sometimes have had only 2 weeks training.
At Ledgerline, a highly qualified CPA with a Masters in Taxation does your work from start to finish.
**I don't need it to say exactly this but I want the theme of the flyer to have these points in it.
Nice to have
• Something different

```html
<!DOCTYPE html>
<html lang="en">
<head>
<meta charset="utf-8">
<title>Ledgerline – Flyer</title>
<link href="https://fonts.googleapis.com/css2?family=Roboto+Condensed:wght@300;400;700&family=Montserrat:wght@500&display=swap" rel="stylesheet">
<style>
  :root {
    --page-bg: #e4e4e3;
    --paper: #ffffff;
    --ink: #2b2b2c;
    --ink-soft: #3a3a3b;
    --bar: #2a2c2e;
    --bar-text: #ffffff;
    --ring: #e6e6e8;
    --photo-light: #eef0f1;
    --photo-mid: #c9ccce;
    --photo-dark: #3b4148;
    --desk: #d9c3a6;
    --badge-blue: #0f5aa3;
    --badge-yellow: #f4d21c;
    --badge-sky: #1fb6e8;
    --badge-lime: #b7d433;
  }
  * { box-sizing: border-box; margin: 0; padding: 0; }
  html, body {
    width: 1045px; height: 1200px; overflow: hidden;
    background: var(--page-bg);
  }
  .flyer {
    position: absolute; left: 119px; top: 30px;
    width: 806px; height: 1140px;
    background: var(--paper);
    overflow: hidden;
    box-shadow: 0 14px 30px rgba(0,0,0,.18);
    font-family: "Roboto Condensed", "Arial Narrow", sans-serif;
    color: var(--ink);
  }
  .portrait {
    position: absolute; inset: 0;
    background:
      radial-gradient(ellipse 260px 330px at 640px 420px, #c99a7f 0%, #b98a70 45%, transparent 70%),
      linear-gradient(180deg, transparent 0 1080px, var(--desk) 1080px),
      radial-gradient(ellipse 360px 620px at 700px 980px, var(--photo-dark) 0 60%, transparent 75%),
      linear-gradient(120deg, var(--photo-light) 0%, #e2e5e7 50%, var(--photo-mid) 100%);
  }
  .panel { position: absolute; inset: 0; }
  .brand {
    position: absolute; left: 0; width: 448px; top: 66px;
    display: flex; flex-direction: column; align-items: center;
  }
  .brand-mark {
    width: 118px; height: 118px; border-radius: 50%;
    border: 3px solid var(--ink);
  }
  .brand-name {
    margin-top: 22px;
    font-family: "Montserrat", sans-serif; font-weight: 500;
    font-size: 36px; letter-spacing: 10px; color: var(--ink);
    white-space: nowrap;
  }
  .pitch { position: absolute; left: 71px; top: 472px; width: 420px; }
  .pitch-question {
    font-weight: 700; font-size: 26px; line-height: 25px;
  }
  .pitch-intro {
    margin-top: 14px; font-weight: 300; font-size: 21px; line-height: 22px;
  }
  .pitch-list { list-style: none; margin-top: 10px; }
  .pitch-list li {
    position: relative; padding-left: 26px;
    font-weight: 300; font-size: 20px; line-height: 25px;
  }
  .pitch-list svg { position: absolute; left: 0; top: 6px; }
  .pitch-claim {
    margin-top: 22px;
    font-weight: 700; font-size: 34px; line-height: 39px;
    text-transform: uppercase; color: var(--ink-soft);
    white-space: nowrap;
  }
  .badges { position: absolute; left: 75px; top: 915px; display: flex; align-items: center; gap: 10px; }
  .badge-member { display: flex; width: 168px; height: 74px; }
  .badge-member .left { flex: 0 0 107px; background: var(--badge-blue); }
  .badge-member .right { flex: 1; background: var(--badge-yellow); }
  .badge-round { width: 80px; height: 80px; border-radius: 50%; }
  .badge-software { background: var(--badge-sky); }
  .badge-register { background: var(--badge-lime); border: 6px solid #f2f2f2; box-shadow: 0 0 0 1px #999; }
  .contact-bar {
    position: absolute; left: 0; right: 0; top: 1028px; height: 73px;
    background: var(--bar); color: var(--bar-text);
    display: flex; align-items: center; justify-content: center;
    font-weight: 700; font-size: 38px; letter-spacing: 2px;
    white-space: nowrap;
  }
  .contact-bar .divider { margin: 0 20px; }
</style>
</head>
<body>
  <main class="flyer">
    <div class="portrait" role="img" aria-label="Photo of a confident accountant in a grey suit and blue tie, hands clasped, in a bright office"></div>

    <svg class="panel" width="806" height="1140" viewBox="0 0 806 1140" aria-hidden="true">
      <circle cx="29" cy="851" r="557" fill="#ffffff" fill-opacity="0.55"/>
      <circle cx="29" cy="851" r="557" fill="none" stroke="var(--ring)" stroke-width="2"/>
      <circle cx="29" cy="851" r="525" fill="#ffffff"/>
      <rect x="0" y="1101" width="806" height="39" fill="#ffffff"/>
    </svg>

    <header class="brand">
      <div class="brand-mark"></div>
      <div class="brand-name">LEDGERLINE</div>
    </header>

    <section class="pitch">
      <h1 class="pitch-question">Do you know who is<br>actually doing your tax?</h1>
      <p class="pitch-intro">Other accounting firms -<br>use junior unqualified staff</p>
      <ul class="pitch-list">
        <li><svg width="16" height="16" viewBox="0 0 16 16"><circle cx="8" cy="8" r="8" fill="var(--ink)"/><path d="M5 5l6 6M11 5l-6 6" stroke="#fff" stroke-width="2"/></svg>Outsource to cheap labour countries</li>
        <li><svg width="16" height="16" viewBox="0 0 16 16"><circle cx="8" cy="8" r="8" fill="var(--ink)"/><path d="M5 5l6 6M11 5l-6 6" stroke="#fff" stroke-width="2"/></svg>Use tax consultants who sometimes<br>have had only 2 weeks training.</li>
      </ul>
      <p class="pitch-claim">At Ledgerline, a highly<br>qualified CPA with a<br>masters in taxation<br>does your work from<br>start to finish.</p>
    </section>

    <div class="badges">
      <div class="badge-member"><span class="left"></span><span class="right"></span></div>
      <div class="badge-round badge-software"></div>
      <div class="badge-round badge-register"></div>
    </div>

    <footer class="contact-bar">
      <span class="phone">0417 582 396</span><span class="divider">|</span><span class="web">WWW.LEDGERLINE.COM.AU</span>
    </footer>
  </main>
</body>
</html>
```